Torquel Australia Pty Ltd

I require professional business cards with our company logo. We would like something that looks sharp and unique. I have attached the logo for our business, which is an industrial electrical contracting company. But this does not need to be shown on the cards.

Industry/Entity Type

Industrial

Requirements
Must have
• The design must be double sided and needs to have one side with our logo only and the other side with our details.
Should not have
• We do not want any lightening bolts on the designs as this is very common.

```html
<!DOCTYPE html>
<html lang="en">
<head>
<meta charset="utf-8">
<title>Torquel Australia Pty Ltd – Business Cards</title>
<link rel="stylesheet" href="https://fonts.googleapis.com/css2?family=Open+Sans:wght@400;600;700&display=swap">
<style>
  :root {
    --backdrop: #a8978a;
    --card-black: #0c0c0c;
    --card-white: #f1f1f1;
    --gold: #c99a2e;
    --gold-light: #f3d27a;
    --gold-dark: #8a6214;
    --ink: #111111;
    --ink-soft: #333333;
  }
  * { margin: 0; padding: 0; box-sizing: border-box; }
  html, body {
    width: 1200px; height: 694px; overflow: hidden;
    background: var(--backdrop);
    font-family: "Open Sans", Arial, sans-serif;
  }
  .canvas { position: relative; width: 1200px; height: 694px; }

  .card {
    position: absolute; top: 220px;
    width: 464px; height: 265px;
    border-radius: 10px; overflow: hidden;
  }
  .card--front { left: 77px; background: var(--card-black); }
  .card--back { left: 671px; background: var(--card-white); }

  .card-art { position: absolute; inset: 0; width: 464px; height: 265px; }

  .brand { position: absolute; color: var(--gold); font-weight: 700; line-height: 1; }
  .brand-dot {
    position: absolute; border: 3px solid var(--gold); border-radius: 50%;
  }
  .brand-name { position: absolute; letter-spacing: 3px; white-space: nowrap; }
  .brand-sub { position: absolute; letter-spacing: 5.2px; white-space: nowrap; }

  /* front */
  .card--front .brand-dot { left: 106px; top: 100px; width: 60px; height: 60px; }
  .card--front .brand-name { left: 178px; top: 112px; font-size: 29px; }
  .card--front .brand-sub { left: 179px; top: 144px; font-size: 9px; letter-spacing: 4px; }

  /* back */
  .card--back .brand-dot { left: 86px; top: 75px; width: 60px; height: 60px; }
  .card--back .brand-name { left: 20px; top: 150px; width: 192px; text-align: center; font-size: 26px; }
  .card--back .brand-sub { left: 20px; top: 180px; width: 192px; text-align: center; font-size: 8.5px; letter-spacing: 3.4px; }

  .person { position: absolute; right: 20px; top: 60px; text-align: right; color: var(--ink); }
  .person-name { font-size: 17px; font-weight: 700; letter-spacing: 2.4px; }
  .person-role { font-size: 12px; font-weight: 400; letter-spacing: 1.6px; margin-top: 3px; color: var(--ink-soft); }

  .contact {
    position: absolute; right: 42px; text-align: right;
    font-size: 8.5px; font-weight: 700; line-height: 16px; color: var(--ink);
    letter-spacing: 0.3px; white-space: nowrap;
  }
  .contact--address { top: 125px; }
  .contact--phone { top: 171px; }
  .contact--web { top: 216px; letter-spacing: 0.6px; }

  .icon { position: absolute; right: 20px; width: 12px; height: 12px; fill: var(--ink); }
</style>
</head>
<body>
<main class="canvas">

  <section class="card card--front" aria-label="Card front">
    <div class="brand">
      <span class="brand-dot"></span>
      <span class="brand-name">TORQUEL</span>
      <span class="brand-sub">AUSTRALIA PTY LTD</span>
    </div>
  </section>

  <section class="card card--back" aria-label="Card back">
    <svg class="card-art" viewBox="0 0 464 265" aria-hidden="true">
      <defs>
        <linearGradient id="goldBand" x1="0" y1="0" x2="0" y2="1">
          <stop offset="0" stop-color="var(--gold-dark)"/>
          <stop offset="0.35" stop-color="var(--gold-light)"/>
          <stop offset="0.6" stop-color="var(--gold)"/>
          <stop offset="1" stop-color="var(--gold-light)"/>
        </linearGradient>
      </defs>
      <path d="M0 0 H190 Q255 132 192 265 H0 Z" fill="url(#goldBand)"/>
      <path d="M0 0 H138 Q240 132 165 265 H0 Z" fill="var(--card-black)"/>
    </svg>

    <div class="brand">
      <span class="brand-dot"></span>
      <span class="brand-name">TORQUEL</span>
      <span class="brand-sub">AUSTRALIA PTY LTD</span>
    </div>

    <div class="person">
      <p class="person-name">HAMISH DELANEY</p>
      <p class="person-role">DIRECTOR</p>
    </div>

    <p class="contact contact--address">PO BOX 318<br>MERIDEN NSW 2571</p>
    <svg class="icon" style="top:126px" viewBox="0 0 12 12" aria-hidden="true">
      <path d="M6 0.5a4 4 0 0 0-4 4c0 3 4 7 4 7s4-4 4-7a4 4 0 0 0-4-4zm0 5.6a1.6 1.6 0 1 1 0-3.2 1.6 1.6 0 0 1 0 3.2z"/>
    </svg>

    <p class="contact contact--phone">02 4711 0392<br>0412 305 774</p>
    <svg class="icon" style="top:172px" viewBox="0 0 12 12" aria-hidden="true">
      <path d="M1 4.5C1 2.5 3 1.5 6 1.5s5 1 5 3l-2.2.6-.6-1.4H3.8l-.6 1.4zM3 6h6l1 4H2z"/>
    </svg>
    <svg class="icon" style="top:186px;height:14px" viewBox="0 0 12 14" aria-hidden="true">
      <path d="M3.5 0.5h5a1 1 0 0 1 1 1v11a1 1 0 0 1-1 1h-5a1 1 0 0 1-1-1v-11a1 1 0 0 1 1-1zm0.3 1.5v8.5h4.4V2zM6 11.2a.7.7 0 1 0 0 1.4.7.7 0 0 0 0-1.4z"/>
    </svg>

    <p class="contact contact--web">HAMISH@TORQUELAUSTRALIA.COM.AU<br>WWW.TORQUELAUSTRALIA.COM.AU</p>
    <svg class="icon" style="top:218px" viewBox="0 0 12 12" aria-hidden="true">
      <path d="M1 3h10v6.5H1zM1.6 3.6 6 7l4.4-3.4" fill="none" stroke="var(--ink)" stroke-width="1.1"/>
    </svg>
    <svg class="icon" style="top:234px" viewBox="0 0 12 12" aria-hidden="true">
      <g fill="none" stroke="var(--ink)" stroke-width="1.1">
        <circle cx="6" cy="6" r="5"/>
        <ellipse cx="6" cy="6" rx="2.2" ry="5"/>
        <path d="M1 6h10"/>
      </g>
    </svg>
  </section>

</main>
</body>
</html>
```